CrestwayGuides Summer Brunch

This flyer is designed to market the upcoming conference in July

Target Market(s)

African American Christian Men and Women

Font styles to use
Decorative

Requirements
Must have
• This flyer is to represent both men and women as follows:
• Although offered on the same day and same location - Men and Women must appear two meetings in one location
• 1. SOB - Sons of Bright
• 2. GAVU - Gentle and Very Uplifted - Women
• Theme: "2020 - Rising With Grace" (Ephesians 6:10-15)
• Date: June 27, 2020
Nice to have
• *Distinct between the two meetings in one
• * Unified brand coupled with Men and Women targets
• * Vibrant, energized, active flyer to communicate promise and hope
Should not have
• Profanity, clip art, etc.

```html
<!DOCTYPE html>
<html lang="en">
<head>
<meta charset="utf-8">
<title>CrestwayGuides – GAVU &amp; SOB Conference 2020</title>
<link rel="stylesheet" href="https://fonts.googleapis.com/css2?family=Crimson+Pro:ital,wght@0,400;0,600;0,700;1,600;1,700&display=swap">
<style>
  :root {
    --ink: #0b0b0b;
    --paper: #ffffff;
    --gold: #c4972e;
    --olive-gold: #8d7a3c;
    --rust: #c24a1a;
    --slate: #9d9d9d;
    --sage: #8b8a6c;
    --stage: #d6d6d6;
  }
  html, body {
    margin: 0;
    width: 1200px;
    height: 1200px;
    overflow: hidden;
    background: var(--stage);
  }
  .flyer {
    position: absolute;
    left: 150px;
    top: 20px;
    width: 900px;
    height: 1160px;
    font-family: "Crimson Pro", Georgia, serif;
  }
  .t-white { fill: var(--paper); }
  .t-gold { fill: var(--gold); }
  .t-ink { fill: var(--ink); }
  .bold { font-weight: 700; }
  .semi { font-weight: 600; }
  .italic { font-style: italic; }
</style>
</head>
<body>
<svg class="flyer" viewBox="0 0 866 1116" xmlns="http://www.w3.org/2000/svg">
  <defs>
    <linearGradient id="field-glow" x1="0" y1="0" x2="0.3" y2="1">
      <stop offset="0" stop-color="#eeeae4"/>
      <stop offset="0.45" stop-color="#b89a6a"/>
      <stop offset="1" stop-color="#3a2e1c"/>
    </linearGradient>
    <linearGradient id="sunset-sky" x1="0" y1="0" x2="0" y2="1">
      <stop offset="0" stop-color="#5a3a4a"/>
      <stop offset="0.35" stop-color="#e9932a"/>
      <stop offset="0.6" stop-color="#c8785e"/>
      <stop offset="1" stop-color="#4a2e44"/>
    </linearGradient>
    <linearGradient id="footer-band" x1="0" y1="0" x2="1" y2="0">
      <stop offset="0" stop-color="#0b0b0b"/>
      <stop offset="0.45" stop-color="#2a2215"/>
      <stop offset="1" stop-color="#9a7a36"/>
    </linearGradient>
    <clipPath id="flyer-clip"><rect width="866" height="1116"/></clipPath>
  </defs>

  <g clip-path="url(#flyer-clip)">
    <rect class="base" width="866" height="1116" fill="var(--paper)"/>

    <!-- header -->
    <polygon class="header-dark" points="0,0 501,0 486,75 0,75" fill="var(--ink)"/>
    <rect class="header-rule" x="0" y="75" width="866" height="8" fill="var(--gold)"/>
    <rect x="0" y="34" width="64" height="5" fill="var(--paper)"/>
    <text class="t-white bold" x="78" y="54" font-size="50">GAVU</text>
    <text x="794" y="54" font-size="50" class="bold" fill="var(--olive-gold)" text-anchor="end">SOB</text>
    <rect x="806" y="34" width="60" height="5" fill="var(--olive-gold)"/>

    <!-- image areas -->
    <polygon class="photo-women" role="img" aria-label="Photo: a woman dancing in a sunlit field at golden hour"
      points="0,83 486,83 415,397 0,397" fill="url(#field-glow)"/>
    <polygon class="photo-men" role="img" aria-label="Photo: a man with raised arms on a rocky peak against a sunset sky over the sea"
      points="486,83 866,83 866,397 415,397" fill="url(#sunset-sky)"/>
    <polygon class="accent-sage" points="0,258 150,397 0,397" fill="var(--sage)"/>

    <!-- women panel -->
    <polygon class="panel-women" points="0,397 378,567 325,848 0,848" fill="var(--ink)"/>

    <!-- theme band -->
    <polygon class="theme-band" points="0,397 866,397 866,567 318,567" fill="var(--rust)"/>
    <text class="t-white bold" x="156" y="459" font-size="66">2020</text>
    <text class="t-white semi" x="315" y="457" font-size="31">Conference Theme:</text>
    <text class="t-white" x="315" y="512" font-size="52">Rising With <tspan class="bold">GRACE</tspan></text>
    <polygon class="scripture-tag" points="628,523 866,523 866,561 620,561" fill="var(--ink)"/>
    <text class="t-white semi italic" x="831" y="549" font-size="22" text-anchor="end">Ephesians 6:10-15</text>

    <!-- women title -->
    <text class="t-gold bold" x="167" y="598" font-size="50" text-anchor="middle">GAVU</text>
    <g class="t-white bold" font-size="40" text-anchor="middle">
      <text x="167" y="647">Gentle</text>
      <text x="167" y="697">And</text>
      <text x="167" y="748">Very Uplifted</text>
      <text x="167" y="799" class="italic">Women</text>
    </g>

    <!-- men panel -->
    <polygon class="panel-men" points="378,567 866,567 866,722 348,722" fill="var(--slate)"/>
    <text class="t-white bold" x="622" y="644" font-size="50" text-anchor="middle">SOB</text>
    <text class="t-white semi" x="626" y="693" font-size="42" text-anchor="middle"><tspan class="italic">Sons</tspan> Of Bright</text>

    <!-- venue -->
    <g class="t-ink semi" font-size="19" text-anchor="middle">
      <text x="628" y="751">Both Men &amp; Women Conference will be held</text>
      <text x="628" y="775">on the same day and venue:</text>
    </g>
    <circle cx="449" cy="822" r="38" fill="var(--gold)"/>
    <path class="icon-pin" d="M449 800 a13 13 0 0 1 13 13 c0 10 -13 26 -13 26 s-13 -16 -13 -26 a13 13 0 0 1 13 -13 z" fill="var(--paper)"/>
    <circle cx="449" cy="813" r="5" fill="var(--gold)"/>
    <text class="t-ink semi" x="505" y="834" font-size="33">Venue Address</text>

    <!-- date block -->
    <polygon class="date-block" points="0,848 325,848 296,1003 0,1003" fill="var(--gold)"/>
    <circle cx="150" cy="882" r="24" fill="none" stroke="var(--paper)" stroke-width="3"/>
    <path class="icon-clock" d="M150 868 V883 L161 888" fill="none" stroke="var(--paper)" stroke-width="3" stroke-linecap="round"/>
    <text class="t-white bold" x="147" y="950" font-size="39" text-anchor="middle">27 JUNE 2020</text>
    <text class="t-white semi" x="147" y="983" font-size="28" text-anchor="middle">10:00AM-14:00PM</text>

    <!-- footer -->
    <rect class="footer" x="0" y="1008" width="866" height="108" fill="url(#footer-band)"/>
    <g class="t-white semi" font-size="20">
      <text x="35" y="1053">For RSVP please contact us at <tspan class="t-gold">555-014-2737</tspan></text>
      <text x="31" y="1078">or via our website: <tspan class="t-gold">www.crestwayguides.com</tspan></text>
    </g>

    <!-- brand seal -->
    <circle class="brand-seal" cx="663" cy="1092" r="202" fill="var(--ink)" stroke="var(--gold)" stroke-width="6"/>
    <text class="t-white" x="663" y="1058" font-size="44" text-anchor="middle">CrestwayGuides</text>
  </g>
</svg>
</body>
</html>
```